Plakat-Design für Pfandhaus gesucht
Zielgruppe
Wir sind ein Pfandhaus wir vergeben Pfandkredite gegen Wertgegenstände sowie Juwelier und Goldankauf aber in erster Linie steht das Pfandhaus .
Aufgabenstellung
Ich möchte gerne Plakate Buchen die an Straßen oder Hauswänden befestigt sind. Ca.3,5x3 Meter. Die Botschaft muss kurz und knapp sein da die Leute ja vorbeifahren.

```html
<!DOCTYPE html>
<html lang="de">
<head>
<meta charset="utf-8">
<title>Plakat Pfandhaus</title>
<link href="https://fonts.googleapis.com/css2?family=League+Gothic&display=swap" rel="stylesheet">
<style>
  :root {
    --red: #e2183a;
    --white: #ffffff;
    --charcoal: #474645;
    --ink: #2f2f2f;
    --gold: #b8a36a;
    --page: #f1f1ef;
    --photo-dark: #3f5654;
    --photo-mid: #8d9593;
    --photo-light: #d9d8d4;
  }
  html, body {
    margin: 0;
    width: 849px;
    height: 1200px;
    overflow: hidden;
    background: var(--page);
    font-family: "League Gothic", "Oswald", sans-serif;
  }
  .poster {
    position: absolute;
    left: 20px;
    top: 253px;
    width: 809px;
    height: 694px;
    background: var(--white);
    box-shadow: 0 6px 18px rgba(0,0,0,.25);
    overflow: hidden;
  }
  .photo {
    position: absolute;
    left: 0; top: 0;
    width: 809px; height: 485px;
    background:
      radial-gradient(ellipse at 45% 45%, var(--photo-light) 0%, var(--photo-mid) 55%, transparent 80%),
      linear-gradient(90deg, var(--photo-dark) 0%, var(--photo-mid) 35%, var(--photo-light) 60%, #5c86a0 82%, #3f6f8c 100%);
  }
  .headline span {
    position: absolute;
    display: inline-block;
    line-height: 1;
    padding: 0 6px;
    text-transform: uppercase;
    white-space: nowrap;
  }
  .hl-red { background: var(--white); color: var(--red); }
  .hl-dark { background: var(--charcoal); color: var(--white); }
  .hl-1 { left: 62px; top: 31px; font-size: 112px; }
  .hl-2 { left: 28px; top: 134px; font-size: 66px; }
  .hl-3 { left: 82px; top: 200px; font-size: 66px; }
  .hl-4 { left: 69px; top: 267px; font-size: 112px; }
  .hl-5 { left: 33px; top: 372px; font-size: 96px; }

  .claim-band {
    position: absolute;
    left: 0; top: 485px;
    width: 809px; height: 80px;
    background: var(--white);
    border-top: 3px solid var(--red);
    border-bottom: 3px solid var(--red);
    box-sizing: border-box;
  }
  .claim {
    position: absolute;
    left: 22px; top: 6px;
    margin: 0;
    font-size: 62px;
    line-height: 1;
    font-weight: 400;
    color: var(--ink);
    white-space: nowrap;
  }
  .claim em { font-style: normal; color: var(--red); }

  .member-badge {
    position: absolute;
    left: 701px; top: 433px;
    width: 85px; height: 116px;
  }

  .contact-bar {
    position: absolute;
    left: 0; top: 565px;
    width: 809px; height: 129px;
    background: var(--charcoal);
  }
  .brand {
    position: absolute;
    left: 23px; top: 12px;
    width: 191px; height: 92px;
    border: 1px solid var(--gold);
    box-sizing: border-box;
    display: flex;
    flex-direction: column;
    align-items: center;
    justify-content: center;
    color: var(--gold);
    font-size: 26px;
    line-height: 1.05;
    text-align: center;
  }
  .address {
    position: absolute;
    left: 247px; top: 10px;
    margin: 0;
    font-size: 49px;
    line-height: 0.95;
    color: var(--gold);
    font-style: normal;
    white-space: nowrap;
  }
  .web {
    position: absolute;
    right: 0; bottom: 0;
    width: 196px; height: 44px;
    background: var(--gold);
    clip-path: polygon(12% 0, 100% 0, 100% 100%, 0 100%);
    color: var(--ink);
    font-size: 22px;
    line-height: 44px;
    text-align: right;
    padding-right: 14px;
    box-sizing: border-box;
  }
</style>
</head>
<body>
  <main class="poster">
    <div class="photo" role="img" aria-label="Foto: Mann in weißem T-Shirt und Jeans zieht seine leere Hosentasche heraus"></div>

    <h1 class="headline">
      <span class="hl-red hl-1">Jeder</span>
      <span class="hl-dark hl-2">kann mal</span>
      <span class="hl-dark hl-3">einen</span>
      <span class="hl-red hl-4">Engpass</span>
      <span class="hl-red hl-5">haben!</span>
    </h1>

    <div class="claim-band">
      <p class="claim">Wir helfen. <em>Schnell und unbürokratisch.</em></p>
    </div>

    <svg class="member-badge" viewBox="0 0 85 116" aria-label="Verbandsabzeichen">
      <rect x="0" y="0" width="85" height="116" fill="#ffffff" stroke="#dddddd"/>
      <rect x="14" y="16" width="57" height="57" fill="#e2183a"/>
    </svg>

    <footer class="contact-bar">
      <div class="brand"><span>Martin Lenz</span><span>Pfandkredit</span></div>
      <address class="address">Ahornweg 7 · 66113 Saarbrücken<br>Tel.: 06 81 / 12 345 678</address>
      <div class="web">www.pfandkredit-lenz.de</div>
    </footer>
  </main>
</body>
</html>
```